Infographics about Quarnel Census

Hello, we are Plenvoria, a leading Big Data and Data Science consultancy firm from The Netherlands. We are looking for an awesome infographic.

Introduction
In order to create a better understanding of the status of Big Data in our little country, together with the biggest Big Data trade show Quarnel Fair, we created the Quarnel Census. This first national research on Big Data aims at providing insight in use of Big Data. The survey is built on five corner stones: Organization, Data, Technology, Skills and Process.

Design
We are looking for an insightful representation of the key-results of the survey, based on the five corner stones. It may also very well be multiple infographics in order to decrease the information density, but I'll leave that to you.

We are looking for a fresh, funky and attractive design, that is easily understood. Please use the colors (orange and blue) of the survey report. For more information see: http://www.plenvoria-example.com/static/images/quarnelcensus/quarnelcensus-uitkomst-web.pdf

```html
<!DOCTYPE html>
<html lang="en">
<head>
<meta charset="utf-8">
<title>Infographic of Quarnel Census</title>
<link href="https://fonts.googleapis.com/css2?family=Oswald:wght@400;600;700&family=Open+Sans:wght@400;600;700;800&display=swap" rel="stylesheet">
<style>
:root{
  --blue:#3274b5;
  --blue-deep:#245f9c;
  --blue-soft:#c9d7e6;
  --orange:#f7931e;
  --orange-deep:#d9771a;
  --red:#e8532b;
  --grey:#eef0f3;
  --grey-mid:#c8ccd2;
  --ink:#333a42;
  --white:#ffffff;
}
*{box-sizing:border-box;margin:0;padding:0}
html,body{width:1200px;height:5233px;overflow:hidden}
body{background:var(--white);font-family:"Open Sans",Arial,sans-serif;color:var(--ink);position:relative}
.abs{position:absolute}
.section{position:absolute;left:0;width:1200px}
.header{top:0;height:270px;background:var(--blue);text-align:center;color:var(--white)}
.header h1{font-family:"Oswald",Arial,sans-serif;font-weight:700;font-size:60px;letter-spacing:1px;padding-top:48px;text-transform:uppercase}
.header p{font-size:22px;margin-top:6px;opacity:.9}
.band{height:100px;background:var(--grey);display:flex;align-items:center;justify-content:center}
.band::before{content:"";position:absolute;left:0;right:0;top:44px;height:12px;background:var(--blue-deep)}
.ribbon{position:relative;background:var(--orange);color:var(--white);font-family:"Oswald",Arial,sans-serif;font-weight:600;font-size:46px;letter-spacing:1px;text-transform:uppercase;padding:2px 50px;line-height:64px}
.num{position:absolute;width:72px;height:72px;border-radius:50%;background:var(--white);border:4px solid var(--blue-deep);font-family:"Oswald",Arial,sans-serif;font-size:28px;font-weight:600;color:var(--ink);display:flex;align-items:center;justify-content:center}
.title{position:absolute;font-weight:800;font-size:31px;line-height:1.2}
.txt{position:absolute;font-size:20px;line-height:1.45}
.blue-bg{background:var(--blue);color:var(--white)}
.grey-bg{background:var(--grey)}
.white-bg{background:var(--white)}
.divider{position:absolute;left:40px;right:40px;height:2px;background:rgba(255,255,255,.35)}
.divider.dark{background:var(--grey-mid)}
.vdivider{position:absolute;top:30px;width:2px;background:rgba(255,255,255,.35)}
.donut{position:absolute}
.donut text{font-family:"Open Sans",Arial,sans-serif;font-weight:800}
.stat{position:absolute;font-size:17px}
.stat b{font-weight:800;margin-right:10px}
.minibar{display:flex;gap:3px;margin-top:6px}
.minibar i{display:block;width:11px;height:11px;background:var(--grey-mid)}
.minibar i.on{background:var(--orange)}
.ring-stat{position:absolute;text-align:center;font-size:17px;font-weight:600}
.ring-stat .ring{width:82px;height:82px;border-radius:50%;border:6px solid var(--orange);background:var(--white);color:var(--orange);font-weight:800;font-size:22px;display:flex;align-items:center;justify-content:center;margin:0 auto 8px}
.blocks{display:flex;gap:4px}
.blocks i{display:block;width:26px;height:26px;background:var(--grey-mid)}
.blocks i.on{background:var(--orange)}
.challenge{position:absolute;left:95px;font-size:20px}
.challenge b{font-weight:800;margin-right:22px}
.tech-box{position:absolute;width:240px;height:74px;border:2px solid var(--grey-mid);background:var(--white);display:flex;align-items:center;padding-left:14px;gap:14px}
.tech-box b{font-size:30px;font-weight:800;color:var(--blue-deep)}
.tech-box span{font-size:22px;font-weight:700;color:var(--blue)}
.profile{position:absolute;left:690px;display:flex;align-items:center;gap:26px;font-size:20px;line-height:1.4;width:460px}
.profile .ring{flex:none;width:78px;height:78px;border-radius:50%;border:5px solid var(--orange);color:var(--orange);font-weight:800;font-size:20px;display:flex;align-items:center;justify-content:center}
.plist{position:absolute;left:530px;width:620px}
.plist div{display:flex;font-size:18px;line-height:1.35;margin-bottom:16px}
.plist b{color:var(--orange);font-weight:800;width:70px;flex:none;font-size:20px}
.orange{color:var(--orange)}
.usage{position:absolute;left:130px;width:940px;height:300px;background:var(--white);color:var(--ink)}
.usage h3{position:absolute;left:130px;top:30px;font-size:36px;font-weight:800;color:var(--orange)}
.usage .col{position:absolute;top:96px;width:370px}
.usage .col h4{font-size:24px;font-weight:800;padding-bottom:8px;border-bottom:3px solid var(--orange);margin-bottom:10px}
.usage .col div{display:flex;font-size:22px;padding:8px 0;border-bottom:1px solid var(--grey-mid)}
.usage .col b{color:var(--orange);width:70px;font-weight:800}
.footer{top:5010px;height:223px;background:var(--white);display:flex;align-items:center;justify-content:space-around;padding:0 60px}
.brand{display:flex;align-items:center;gap:14px;font-size:38px;font-weight:700;color:var(--blue-deep)}
.brand .sq{width:40px;height:40px;background:var(--blue-deep)}
.brand .ci{width:44px;height:44px;border-radius:50%;background:var(--blue-deep)}
</style>
</head>
<body>

<header class="section header">
  <h1>Infographic of Quarnel Census</h1>
  <p>Source Quarnel Census 2016, 166 participants</p>
</header>

<!-- ORGANIZATION -->
<div class="section band" style="top:270px"><div class="ribbon">Organization</div></div>
<section class="section blue-bg" style="top:370px;height:810px">
  <div class="num" style="left:50px;top:40px">01</div>
  <div class="title" style="left:150px;top:44px;width:400px">Opportunities Of Data</div>
  <svg class="donut" style="left:90px;top:140px" width="160" height="160" viewBox="0 0 160 160">
    <circle cx="80" cy="80" r="60" fill="none" stroke="#fff" stroke-width="24"/>
    <circle cx="80" cy="80" r="60" fill="none" stroke="#f7931e" stroke-width="24" stroke-dasharray="347 377" transform="rotate(-90 80 80)"/>
    <text x="80" y="91" text-anchor="middle" fill="#fff" font-size="32">92%</text>
  </svg>
  <p class="txt" style="left:290px;top:170px;width:270px">92% of organizations say that the opportunities of data for their organization are big.</p>

  <div class="vdivider" style="left:600px;height:320px"></div>

  <div class="num" style="left:640px;top:40px">02</div>
  <div class="title" style="left:740px;top:60px">Budget</div>
  <svg class="donut" style="left:700px;top:140px" width="160" height="160" viewBox="0 0 160 160">
    <circle cx="80" cy="80" r="60" fill="none" stroke="#fff" stroke-width="24"/>
    <circle cx="80" cy="80" r="60" fill="none" stroke="#f7931e" stroke-width="24" stroke-dasharray="260 377" transform="rotate(-90 80 80)"/>
    <text x="80" y="91" text-anchor="middle" fill="#fff" font-size="32">69%</text>
  </svg>
  <p class="txt" style="left:890px;top:170px;width:270px">69% of organizations will increase their budget for big data in 2016</p>

  <div class="divider" style="top:380px"></div>

  <div class="num" style="left:50px;top:420px">03</div>
  <div class="title" style="left:150px;top:418px;width:420px">Is Big Data part of your organization strategy?</div>
  <div class="stat" style="left:90px;top:570px"><b>27%</b>agree<div class="minibar"><i class="on"></i><i class="on"></i><i class="on"></i><i></i><i></i><i></i><i></i><i></i><i></i><i></i></div></div>
  <div class="stat" style="left:340px;top:570px"><b>27%</b>partially agree<div class="minibar"><i class="on"></i><i class="on"></i><i class="on"></i><i></i><i></i><i></i><i></i><i></i><i></i><i></i></div></div>
  <div class="stat" style="left:90px;top:650px"><b>11%</b>partially disagree<div class="minibar"><i class="on"></i><i></i><i></i><i></i><i></i><i></i><i></i><i></i><i></i><i></i></div></div>
  <div class="stat" style="left:340px;top:650px"><b>12%</b>totally disagree<div class="minibar"><i class="on"></i><i></i><i></i><i></i><i></i><i></i><i></i><i></i><i></i><i></i></div></div>

  <div class="vdivider" style="left:600px;top:410px;height:360px"></div>

  <div class="num" style="left:640px;top:420px">04</div>
  <div class="title" style="left:740px;top:438px">Success Factors</div>
  <p class="txt" style="left:660px;top:560px;width:250px;font-size:17px">The most important factors of a successful implementation of a big data strategy are:</p>
  <div class="ring-stat" style="left:910px;top:540px;width:120px">
    <div class="ring">28%</div>Company Vision
  </div>
  <div class="ring-stat" style="left:1030px;top:540px;width:150px">
    <div class="ring">19%</div>Support from the management
  </div>
  <p class="txt" style="left:660px;top:710px;width:500px;text-align:center;font-size:17px">These factors are more important than:<br><b class="orange" style="font-size:22px">Budget, Training, Talent</b></p>
</section>

<!-- DATA -->
<div class="section band" style="top:1180px"><div class="ribbon">Data</div></div>
<section class="section grey-bg" style="top:1280px;height:830px">
  <div class="num" style="left:50px;top:40px">01</div>
  <div class="title" style="left:150px;top:40px;width:420px">What Are The Biggest Challenges In The Field Of Data?</div>
  <p class="txt" style="left:95px;top:170px;width:470px;font-size:18px">Only 8% of organizations find optimizing a predictive model the most difficult challenge in the field of data. Top 3 challenges are:</p>
  <div class="challenge" style="top:290px"><b>18%</b>Time to experiment<div class="blocks" style="margin-top:8px"><i class="on"></i><i class="on"></i><i></i><i></i><i></i><i></i><i></i><i></i><i></i><i></i></div></div>
  <div class="challenge" style="top:380px"><b>15%</b>Making data available<div class="blocks" style="margin-top:8px"><i class="on"></i><i class="on"></i><i></i><i></i><i></i><i></i><i></i><i></i><i></i><i></i></div></div>
  <div class="challenge" style="top:470px"><b>14%</b>Investing in data scientists<div class="blocks" style="margin-top:8px"><i class="on"></i><i></i><i></i><i></i><i></i><i></i><i></i><i></i><i></i><i></i></div></div>

  <div class="vdivider" style="left:600px;height:520px;background:var(--grey-mid)"></div>

  <div class="num" style="left:640px;top:40px">02</div>
  <div class="title" style="left:740px;top:58px">Most Used Data Sources</div>
  <p class="txt" style="left:640px;top:150px;width:520px;text-align:center;font-size:22px;font-weight:600">THE MOST USED DATA SOURCES ARE</p>
  <div class="ring-stat" style="left:720px;top:200px;width:170px"><div class="ring">18%</div>CRM / Customer data</div>
  <div class="ring-stat" style="left:920px;top:200px;width:170px"><div class="ring">18%</div>Website statistics</div>
  <p class="txt" style="left:640px;top:365px;width:520px;text-align:center;font-size:38px;font-weight:600">LEAST USED ARE</p>
  <div class="ring-stat" style="left:750px;top:440px;width:100px"><div class="ring">2%</div>Audio</div>
  <div class="ring-stat" style="left:850px;top:440px;width:100px"><div class="ring">5%</div>Video</div>
  <div class="ring-stat" style="left:950px;top:440px;width:100px"><div class="ring">6%</div>Image</div>

  <div class="divider dark" style="top:580px"></div>

  <div class="num" style="left:150px;top:610px">03</div>
  <div class="title" style="left:100px;top:700px">Data Security</div>
  <p class="txt" style="left:100px;top:745px;width:360px;font-size:18px">Are data stored securely within your organization?</p>
  <div class="stat" style="left:490px;top:640px"><b>25%</b>Agrees<div class="minibar"><i class="on"></i><i class="on"></i><i class="on"></i><i></i><i></i><i></i><i></i><i></i><i></i><i></i></div></div>
  <div class="stat" style="left:810px;top:640px"><b>32%</b>Partially Agrees<div class="minibar"><i class="on"></i><i class="on"></i><i class="on"></i><i></i><i></i><i></i><i></i><i></i><i></i><i></i></div></div>
  <div class="stat" style="left:490px;top:730px"><b>12%</b>Partially Disagrees<div class="minibar"><i class="on"></i><i></i><i></i><i></i><i></i><i></i><i></i><i></i><i></i><i></i></div></div>
  <div class="stat" style="left:810px;top:730px"><b>7%</b>Totally Agrees<div class="minibar"><i class="on"></i><i></i><i></i><i></i><i></i><i></i><i></i><i></i><i></i><i></i></div></div>
</section>

<!-- TECHNOLOGY -->
<div class="section band" style="top:2110px"><div class="ribbon">Technology</div></div>
<section class="section white-bg" style="top:2210px;height:820px">
  <div class="num" style="left:50px;top:60px">01</div>
  <div class="title" style="left:190px;top:260px">Type Of Software<br>Used</div>
  <svg class="donut" style="left:40px;top:350px" width="170" height="170" viewBox="0 0 160 160">
    <circle cx="80" cy="80" r="60" fill="none" stroke="#c8ccd2" stroke-width="24"/>
    <circle cx="80" cy="80" r="60" fill="none" stroke="#f7931e" stroke-width="24" stroke-dasharray="170 377" transform="rotate(-90 80 80)"/>
    <text x="80" y="91" text-anchor="middle" fill="#333a42" font-size="32">45%</text>
  </svg>
  <p class="txt" style="left:230px;top:360px;width:320px;font-size:19px">use a mix of <b class="orange">Open Source Software &amp; Licensed Software</b> the rest is divided equally between licensed software and open source</p>

  <div class="vdivider" style="left:600px;height:740px;background:var(--grey-mid)"></div>

  <div class="num" style="left:680px;top:60px">02</div>
  <div class="title" style="left:780px;top:60px">Most Popular<br>Technologies</div>
  <div class="tech-box" style="left:640px;top:220px"><b>21%</b><span>Trunkbase</span></div>
  <div class="tech-box" style="left:910px;top:220px"><b>10%</b><span>Coilscript</span></div>
  <div class="tech-box" style="left:640px;top:360px"><b>8%</b><span>Veltrix</span></div>
  <div class="tech-box" style="left:910px;top:360px"><b>7%</b><span>Statwell</span></div>
  <div class="tech-box" style="left:640px;top:500px"><b>6%</b><span>Anvira</span></div>
  <div class="tech-box" style="left:910px;top:500px"><b>7%</b><span>Loomstudio</span></div>
</section>

<!-- SKILLS -->
<div class="section band" style="top:3030px"><div class="ribbon">Skills</div></div>
<section class="section white-bg" style="top:3130px;height:510px">
  <div class="num" style="left:40px;top:150px">01</div>
  <div class="title" style="left:140px;top:130px;width:420px">What Grade Would You Give The Level Of Knowledge Within Your Organization?</div>
  <p class="txt" style="left:90px;top:320px;font-size:26px">The <b>Average Grade</b> is a <b style="font-size:32px">6</b><br>on a scale of <b style="font-size:32px">10</b></p>
  <div class="blocks abs" style="left:90px;top:420px"><i class="on"></i><i class="on"></i><i class="on"></i><i class="on"></i><i class="on"></i><i class="on"></i><i></i><i></i><i></i><i></i></div>

  <div class="num" style="left:630px;top:20px">02</div>
  <div class="title" style="left:730px;top:20px;width:420px">What Function Profiles Does Your Data Team Consist Of?</div>
  <div class="profile" style="top:160px"><div class="ring">60%</div><span>Over 60% of organizations employ business analysts and/or data analysts</span></div>
  <div class="profile" style="top:280px"><div class="ring">38%</div><span>Only 38% of organizations employ data scientists</span></div>
  <div class="profile" style="top:400px"><div class="ring">17%</div><span>17% is planning to hire data scientists within the next year.</span></div>
</section>

<!-- PROCESS -->
<div class="section band" style="top:3640px"><div class="ribbon">Process</div></div>
<section class="section blue-bg" style="top:3740px;height:1270px">
  <div class="num" style="left:290px;top:30px">01</div>
  <div class="title orange" style="left:230px;top:120px;width:280px;text-align:left">To what extent do you personalize your website?</div>
  <div class="plist" style="top:40px">
    <div><b>46%</b>Do not personalize to website</div>
    <div><b>29%</b>Does this manually</div>
    <div><b>15%</b>Personalizes based on historical data</div>
    <div><b>11%</b>Are able to personalize the website in real-time based on current visitor behavior</div>
  </div>

  <svg class="abs" style="left:390px;top:340px" width="420" height="420" viewBox="0 0 420 420" role="img" aria-label="Ring of four segments">
    <circle cx="210" cy="210" r="175" fill="none" stroke="#f5a623" stroke-width="70" stroke-dasharray="265 835" transform="rotate(-130 210 210)"/>
    <circle cx="210" cy="210" r="175" fill="none" stroke="#c9d7e6" stroke-width="70" stroke-dasharray="265 835" transform="rotate(-40 210 210)"/>
    <circle cx="210" cy="210" r="175" fill="none" stroke="#e3e8ee" stroke-width="70" stroke-dasharray="265 835" transform="rotate(50 210 210)"/>
    <circle cx="210" cy="210" r="175" fill="none" stroke="#e8532b" stroke-width="70" stroke-dasharray="265 835" transform="rotate(140 210 210)"/>
  </svg>

  <div class="num" style="left:140px;top:300px">02</div>
  <div class="title" style="left:40px;top:410px;font-size:27px">Data ethics and value</div>
  <div class="txt" style="left:40px;top:460px;width:340px;font-size:16px">
    <p style="margin-bottom:16px">Only 16% of participants think that consumers are well aware of the data trail they are leaving behind.</p>
    <p style="margin-bottom:16px">Two third of all participants expects that in the future consumers can use data as a form of currency.</p>
    <p>Luckily, 82% of participants agree that companies are responsible for collecting data ethically.</p>
  </div>

  <div class="num" style="left:990px;top:300px">03</div>
  <div class="title orange" style="left:840px;top:400px;width:330px;font-size:25px">Are companies planning to use advanced methods, like deep learning, artificial intelligence and predictive models?</div>
  <div class="plist" style="left:840px;top:580px;width:330px">
    <div><b>17%</b>Are already using these methods</div>
    <div><b>40%</b>Expects these methods to be in production within 3 years</div>
  </div>

  <div class="num" style="left:60px;top:880px">04</div>
  <div class="usage" style="top:880px">
    <h3>What do you use data for?</h3>
    <div class="col" style="left:40px">
      <h4>TOP 3:</h4>
      <div><b>19%</b>Marketing</div>
      <div><b>16%</b>Online</div>
      <div><b>14%</b>Market analysis</div>
    </div>
    <div class="col" style="left:520px">
      <h4>BOTTOM 3:</h4>
      <div><b>3%</b>Human Resource</div>
      <div><b>4%</b>Finance and administration</div>
      <div><b>5%</b>Supply chain &amp; Logistics</div>
    </div>
  </div>
</section>

<footer class="section footer">
  <div class="brand"><span class="sq"></span>Plenvoria</div>
  <div class="brand"><span class="ci"></span>Quarnel Census</div>
  <div class="brand">Quarnel Fair</div>
</footer>

</body>
</html>
```